Sharp, new and modern business flyer

We are an industrial crate manufacturer whose core customer base is in the aeronautical parts sector. We also however build very custom travel show crates and road cases for any spectrum of industries. We have a substantial facility and can accommodate large, production orders so we would like to attract large, local businesses if possible, but ship crates nationwide as well. We have an old tri fold flyer that we have been using for over 3+ years that I will attach for reference but it desperately needs a fresh new look and complete revamp! Our slogan is "Innovative Crating With Superior Service." We are known in the industry as being extremely fast as well as providing excellent customer service and crate design work. We have also in the last year, added two globes to the background of our logo. I am attaching our current business cards that show how we incorporate that. Feel free to visit our website as well as our Facebook page for more info and current pictures. Both are Palbrook-freight.com.

Target Market(s)

Mid to large local business and corporations. Industrial and manufacturing - especially aeronautical or medical (delicate surgical equipment) as well as military.

Industry/Entity Type

Manufacturer

Font styles to use
Sans Serif
Other font styles liked:
• Stencil

Colors

Designer to choose colors to be used in the design.

Requirements
Must have
• 1. Current photos and descriptions of our capabilities. Our most current products are on our Facebook page and our capabilities are on our website.
• 2. Our flyer must state that "All of our quality products are built with lumber that is ISPM 15 Heat Treatment Certified"
• 3. Please add custom pallets as well as on-site crating
Nice to have
• A new, modern look that shows us as current and growing.
Should not have
• Woman owned listed...we are no longer woman owned.

```html
<!DOCTYPE html>
<html lang="en">
<head>
<meta charset="utf-8">
<title>Palbrook Freight – Tri-fold Brochure</title>
<link href="https://fonts.googleapis.com/css2?family=Open+Sans:ital,wght@0,400;0,600;0,700;0,800;1,600&family=Merriweather:wght@700;900&display=swap" rel="stylesheet">
<style>
  :root{
    --yellow:#f2b31b;
    --black:#1d1d1d;
    --ink:#333333;
    --paper:#ffffff;
    --mist:#eeeeee;
    --stage:#e4e4e4;
    --wood-a:#c9a56a;
    --wood-b:#8a8f96;
  }
  *{box-sizing:border-box;margin:0;padding:0}
  html,body{width:1200px;height:2394px;overflow:hidden;background:var(--stage)}
  body{position:relative;font-family:"Open Sans",Arial,sans-serif;color:var(--ink)}

  .spread{position:absolute;left:50px;width:1100px;height:850px;background:var(--paper);overflow:hidden}
  .spread--outside{top:247px}
  .spread--inside{top:1297px}
  .spread__shapes{position:absolute;inset:0;width:1100px;height:850px}
  .fold{position:absolute;top:0;width:1px;height:850px;background:rgba(0,0,0,.08)}

  .photo{position:absolute;background:linear-gradient(135deg,var(--wood-a),var(--wood-b))}
  .photo--cool{background:linear-gradient(160deg,#b7c4cf,#c7a566 55%,#6f6a60)}
  .photo--dark{background:linear-gradient(150deg,#5a4a3a,#2e2a26)}
  .photo--tile{background:linear-gradient(140deg,#d3b98a,#7d746a)}

  .serif{font-family:"Merriweather",Georgia,serif}
  .heading{position:absolute;font-weight:800;text-transform:uppercase;letter-spacing:.5px}
  .body-copy{position:absolute;font-size:11.5px;line-height:1.6}
  .body-copy p+p{margin-top:10px}

  /* outside: about panel */
  .about__title{left:200px;top:262px;color:var(--yellow);font-size:17px}
  .about__copy{left:30px;top:320px;width:310px;color:var(--ink)}
  .about__map{left:24px;top:650px;width:140px;height:90px;background:#9a9a9a;border-radius:4px}
  .about__plan{left:190px;top:650px;width:140px;height:90px;border:2px solid var(--yellow);border-radius:2px}
  .ship-note{position:absolute;font-weight:900;text-transform:uppercase;font-size:12px;line-height:1.35}
  .about__ship{left:30px;top:760px;color:var(--yellow)}

  /* outside: service panel */
  .service__title{left:367px;width:367px;top:50px;text-align:center;color:var(--yellow);font-size:15px;line-height:1.5}
  .service__list{position:absolute;left:392px;top:140px;width:320px;list-style:none;color:#f2f2f2;font-size:11.5px;line-height:1.55}
  .service__list li{position:relative;padding-left:18px;margin-bottom:14px}
  .service__list li::before{content:"";position:absolute;left:0;top:5px;border-left:8px solid var(--yellow);border-top:5px solid transparent;border-bottom:5px solid transparent}
  .service__call{position:absolute;left:367px;width:367px;top:618px;text-align:center;font-style:italic;font-weight:600;font-size:13px;color:var(--black);line-height:1.4;padding:0 40px}
  .brand-square{position:absolute;background:var(--black)}
  .service__square{left:528px;top:672px;width:44px;height:44px}
  .contact{position:absolute;left:400px;top:732px;width:300px;font-size:12px;line-height:1.5;color:var(--ink)}
  .contact__lead{color:var(--yellow);font-weight:700}
  .contact__phone{display:flex;align-items:center;gap:8px;font-size:20px;font-weight:800;color:var(--black)}
  .contact__phone svg{width:20px;height:20px}

  /* outside: cover */
  .brand{position:absolute;display:flex;align-items:center;gap:10px}
  .brand__mark{width:22px;height:22px;background:var(--yellow)}
  .brand__name{font-weight:800;font-size:18px;letter-spacing:1px;color:var(--paper);text-transform:uppercase}
  .cover__brand{left:790px;top:16px}
  .tagline{position:absolute;font-weight:900;text-transform:uppercase;color:var(--black)}
  .cover__tagline{left:770px;top:668px;width:310px;font-size:22px;line-height:1.3}
  .web{position:absolute;font-weight:800;color:var(--yellow);font-size:17px}
  .cover__web{left:770px;top:790px}

  /* inside: products */
  .products__title{left:28px;top:44px;color:var(--yellow);font-size:17px;line-height:1.35}
  .products__list{position:absolute;left:30px;top:112px;list-style:none;color:#f2f2f2;font-size:13px;line-height:1.95}
  .products__list li{position:relative;padding-left:18px}
  .products__list li::before{content:"";position:absolute;left:0;top:8px;border-left:8px solid var(--yellow);border-top:5px solid transparent;border-bottom:5px solid transparent}
  .products__ship{left:30px;top:784px;color:var(--black);font-size:14px}

  /* inside: production */
  .production__title{left:400px;top:54px;color:var(--yellow);font-size:17px}
  .production__copy{left:400px;top:96px;width:305px}
  .band__text{position:absolute;left:430px;top:438px;width:640px;text-align:center;font-size:17px;line-height:1.35;font-weight:900;text-transform:uppercase;color:var(--black)}
  .inside__square{left:992px;top:350px;width:52px;height:52px}
  .grid{position:absolute;display:grid;grid-template-columns:1fr 1fr;gap:12px}
  .grid .photo{position:static;height:96px}
  .grid--left{left:392px;top:560px;width:318px}
  .grid--right{left:758px;top:560px;width:318px}
  .inside__web{left:790px;top:800px;font-size:16px}
</style>
</head>
<body>

<!-- OUTSIDE OF BROCHURE -->
<section class="spread spread--outside">
  <svg class="spread__shapes" viewBox="0 0 1100 850" aria-hidden="true">
    <!-- about panel -->
    <polygon points="0,250 367,205 367,300 0,330" fill="#1d1d1d" opacity="0"/>
    <polygon points="150,250 367,222 367,292 190,300" fill="#1d1d1d"/>
    <polygon points="0,600 367,560 367,850 0,850" fill="#eeeeee"/>
    <polygon points="0,585 110,600 0,640" fill="#1d1d1d"/>
    <polygon points="0,630 140,600 0,700" fill="#f2b31b"/>
    <!-- service panel -->
    <polygon points="367,0 734,0 734,580 367,610" fill="#1d1d1d"/>
    <polygon points="367,610 734,580 734,650 367,680" fill="#f2b31b"/>
    <!-- cover -->
    <polygon points="734,0 1100,0 1100,40 734,70" fill="#1d1d1d"/>
    <polygon points="734,500 900,560 1000,640 734,650" fill="#f2b31b"/>
    <polygon points="1000,520 1100,470 1100,600" fill="#1d1d1d"/>
  </svg>

  <div class="photo photo--cool" style="left:0;top:0;width:367px;height:260px;clip-path:polygon(0 0,100% 0,100% 82%,0 100%)" role="img" aria-label="Photo of workers assembling large wooden crates in the shop"></div>
  <h2 class="heading about__title">About Us</h2>
  <div class="body-copy about__copy">
    <p>Our services include shipping crates, military cases, road cases, heavy equipment skids and custom corrugated boxes. Every crate is designed in-house by our team and built in our own facility, so we can move fast on single units or large production runs for businesses of any size.</p>
    <p>We combine the above with superior service and quick turnaround so your products arrive safe, on time and ready to use.</p>
  </div>
  <div class="photo about__map" role="img" aria-label="Map of the United States"></div>
  <div class="photo about__plan" style="background:none" role="img" aria-label="Line drawing of a crate layout"></div>
  <p class="ship-note serif about__ship">We ship<br>anywhere<br>in the U.S.A.</p>

  <h2 class="heading serif service__title">Innovative Crating<br>With<br>Superior Service</h2>
  <ul class="service__list">
    <li>Product by shipping or by storage, our team designs every crate to fit your part, your schedule and your budget.</li>
    <li>All of our quality products are built with lumber that is ISPM 15 Heat Treatment Certified, ready for export anywhere.</li>
    <li>A growing selection of our product line is stocked and ready to ship, including custom pallets and on-site crating.</li>
    <li>We specialize in fragile, high-value cargo for aerospace, medical and military customers across the country.</li>
    <li>We build large and small orders with the same care, fast lead times and honest pricing.</li>
  </ul>
  <p class="service__call">Please call us with any crating question that you may have.</p>
  <div class="brand-square service__square"></div>
  <div class="contact">
    <p class="contact__lead">To request a quote please call us at:</p>
    <p class="contact__phone">
      <svg viewBox="0 0 24 24"><circle cx="12" cy="12" r="11" fill="none" stroke="#1d1d1d" stroke-width="2"/><path d="M8 6.5l2 .3.8 2.6-1.3 1.1a8 8 0 0 0 3.9 3.9l1.1-1.3 2.6.8.3 2a1.6 1.6 0 0 1-1.7 1.4A10 10 0 0 1 6.6 8.2 1.6 1.6 0 0 1 8 6.5z" fill="#1d1d1d"/></svg>
      (555) 214-7730
    </p>
    <p>info@palbrook-freight.com</p>
    <p>www.palbrook-freight.com</p>
  </div>

  <div class="photo photo--cool" style="left:734px;top:40px;width:366px;height:590px;clip-path:polygon(0 5%,100% 0,100% 80%,0 100%)" role="img" aria-label="Photo of a forklift lifting a large wooden crate, with work gloves in front"></div>
  <div class="brand cover__brand"><span class="brand__mark"></span><span class="brand__name">Palbrook Freight</span></div>
  <p class="tagline serif cover__tagline">We solve customer's product crating and storage problems!</p>
  <p class="web cover__web">www.palbrook-freight.com</p>

  <div class="fold" style="left:367px"></div>
  <div class="fold" style="left:734px"></div>
</section>

<!-- INSIDE OF BROCHURE -->
<section class="spread spread--inside">
  <svg class="spread__shapes" viewBox="0 0 1100 850" aria-hidden="true">
    <polygon points="0,0 367,0 367,470 0,520" fill="#1d1d1d"/>
    <polygon points="0,740 367,700 367,850 0,850" fill="#f2b31b"/>
    <polygon points="367,0 470,0 367,40" fill="#1d1d1d"/>
    <polygon points="367,520 1100,520 1100,850 367,850" fill="#eeeeee"/>
    <polygon points="400,430 1100,410 1100,500 367,510" fill="#f2b31b"/>
    <polygon points="367,430 400,430 367,470" fill="#1d1d1d"/>
  </svg>

  <h2 class="heading products__title">Our Quality Products and<br>Services Include:</h2>
  <ul class="products__list">
    <li>Custom Crates</li>
    <li>Production Crates</li>
    <li>Military Crates</li>
    <li>Custom Corrugated Cardboard Boxes</li>
    <li>Road Cases</li>
    <li>Heavy Equipment Skidding &amp; Crating</li>
    <li>Trade Show Crates &amp; Cases</li>
    <li>Collapsible Crates</li>
    <li>Stretch &amp; Shrink Wrapping</li>
    <li>Shock Control Systems</li>
    <li>International Wood Pallets</li>
  </ul>
  <div class="photo photo--dark" style="left:0;top:500px;width:367px;height:260px;clip-path:polygon(0 8%,100% 0,100% 80%,0 100%)" role="img" aria-label="Photo of stacked dark wooden crates in the warehouse"></div>
  <p class="ship-note serif products__ship">We ship anywhere<br>in the U.S.A.</p>

  <h2 class="heading production__title">Production Crates</h2>
  <div class="body-copy production__copy">
    <p>If you have repeat orders for crates of a fixed size and style, our production line can build them quickly and at a lower cost per unit.</p>
    <p>Our production crating system allows us to assemble and ship large volumes without losing the precision of a custom build.</p>
    <p>Our careful attention to your production schedule allows us to meet your deadlines time after time.</p>
    <p>Production crate savings can be applied to all of our various product lines.</p>
  </div>

  <div class="photo photo--cool" style="left:734px;top:0;width:366px;height:420px" role="img" aria-label="Photo of a forklift moving a wrapped wooden crate outside the facility"></div>
  <div class="brand-square inside__square"></div>
  <p class="band__text serif">We solve customer's product crating<br>and storage problems!</p>

  <div class="grid grid--left">
    <div class="photo photo--tile" role="img" aria-label="Photo of finished crates on the shop floor"></div>
    <div class="photo photo--tile" role="img" aria-label="Photo of a crate with foam inserts"></div>
    <div class="photo photo--tile" role="img" aria-label="Photo of open crate frames"></div>
    <div class="photo photo--tile" role="img" aria-label="Photo of a large closed shipping crate"></div>
  </div>
  <div class="grid grid--right">
    <div class="photo photo--tile" role="img" aria-label="Photo of road cases lined up"></div>
    <div class="photo photo--tile" role="img" aria-label="Photo of a crate interior with padding"></div>
    <div class="photo photo--tile" role="img" aria-label="Photo of stacked wooden crates"></div>
    <div class="photo photo--tile" role="img" aria-label="Photo of pallets ready to ship"></div>
  </div>
  <p class="web inside__web">www.palbrook-freight.com</p>

  <div class="fold" style="left:367px"></div>
  <div class="fold" style="left:734px"></div>
</section>

</body>
</html>
```